Austrian finance und insurance broker needs business card design

We Need a serious looking Design for Business Card. we consult private and corporates customers in finance and insurance questions. the final design should express security and experience. We consult customers in questions of loans, Investments and insurance and have a wide range of Banks to offer. We compare several offers and select the best for our customers.

Target Market(s)

private and coporate customers with efforts in Money and insurance

Industry/Entity Type

Insurance Broker

Contact Information for Business Card

Bernhard Aigner
Geschäftsführer
staatl. geprüfter Vermögensberater und Versicherungsmakler
Tel: 0664 521 8409
office@der-brandl.at
www.der-brandl.at
Leopold Hainz Gasse 14
2183 Melkstetten
GISA Nr. 48270315 u. 51736048 (backside)

Font styles to use
Serif
Sans Serif

Requirements
Must have
• logo (designcrowd zip) and all Details
Nice to have
• makler logo design, maybe a 2 coloured Version is possible

```html
<!DOCTYPE html>
<html lang="de">
<head>
<meta charset="utf-8">
<title>Nordwald Vermögensberatung – Visitenkarte</title>
<link rel="stylesheet" href="https://fonts.googleapis.com/css2?family=Quicksand:wght@500;600;700&display=swap">
<style>
  :root {
    --bg: #e9e7e3;
    --card-white: #f7f7f7;
    --card-grey: #6c6c6c;
    --brand-blue: #2f56a8;
    --text-grey: #555555;
    --text-dark: #333333;
    --seal-red: #c0203a;
    --on-dark: #f2f2f2;
  }
  * { box-sizing: border-box; margin: 0; padding: 0; }
  html, body { width: 1200px; height: 900px; overflow: hidden; }
  body {
    background: var(--bg);
    font-family: "Quicksand", sans-serif;
    display: flex; flex-direction: column; align-items: center; justify-content: center;
    gap: 40px;
  }
  .card {
    position: relative; width: 620px; height: 400px; overflow: hidden;
    box-shadow: 0 6px 18px rgba(0,0,0,0.18);
  }
  .card-front { background: var(--card-white); }
  .card-back { background: var(--card-grey); color: var(--on-dark); }

  .brand { position: absolute; display: flex; align-items: center; gap: 12px; }
  .brand-dot { width: 46px; height: 46px; border-radius: 50%; border: 3px solid var(--brand-blue); flex: none; }
  .brand-name { font-weight: 700; font-size: 17px; color: var(--brand-blue); }
  .brand-tagline { font-weight: 600; font-size: 12px; color: var(--text-grey); margin-top: 2px; }
  .card-front .brand { left: 36px; top: 34px; }
  .card-front .brand-text { border-left: 2px solid var(--text-grey); padding-left: 12px; }

  .person { position: absolute; right: 36px; top: 112px; text-align: right; }
  .person-name { font-weight: 700; font-size: 26px; color: var(--brand-blue); letter-spacing: 0.5px; }
  .person-role { font-weight: 600; font-size: 14px; color: var(--text-grey); margin-top: 10px; }
  .rule { position: absolute; left: 36px; right: 36px; top: 150px; height: 2px; background: var(--brand-blue); }
  .qualification { position: absolute; left: 36px; top: 160px; font-weight: 600; font-size: 14px; color: var(--brand-blue); line-height: 1.2; }

  .contacts { position: absolute; left: 36px; top: 218px; list-style: none; }
  .contacts li { display: flex; align-items: flex-start; gap: 12px; font-weight: 600; font-size: 16px; color: var(--text-dark); margin-bottom: 9px; line-height: 1.15; }
  .contacts svg { width: 15px; height: 15px; flex: none; margin-top: 2px; fill: var(--brand-blue); }

  .seal { position: absolute; right: 70px; bottom: 52px; width: 90px; height: 90px; border-radius: 50%; background: var(--seal-red); }

  .card-back .brand { left: 0; right: 0; top: 112px; flex-direction: column; gap: 14px; text-align: center; }
  .card-back .brand-dot { width: 80px; height: 80px; border-color: var(--on-dark); }
  .card-back .brand-name { color: var(--on-dark); font-size: 24px; }
  .card-back .brand-tagline { color: var(--on-dark); font-size: 16px; }
  .register { position: absolute; left: 0; right: 0; top: 300px; text-align: center; font-weight: 600; font-size: 15px; letter-spacing: 0.5px; }
</style>
</head>
<body>

<section class="card card-front">
  <div class="brand">
    <div class="brand-dot"></div>
    <div class="brand-text">
      <div class="brand-name">Nordwald Vermögensberatung GmbH</div>
      <div class="brand-tagline">Finanzieren, Versichern, Vorsorgen</div>
    </div>
  </div>

  <div class="person">
    <div class="person-name">Bernhard Aigner</div>
    <div class="person-role">Geschäftsführer</div>
  </div>
  <div class="rule"></div>
  <p class="qualification">Staatl. geprüfter Vermögensberater<br>und Versicherungsmakler</p>

  <ul class="contacts">
    <li><svg viewBox="0 0 16 16"><path d="M4 1c1 0 2 3 2 4s-1 1-1 2 2 4 3 4 1-1 2-1 4 1 4 2-1 3-3 3C6 15 1 10 1 4c0-2 2-3 3-3z"/></svg>0664 521 8409</li>
    <li><svg viewBox="0 0 16 16"><path d="M1 3h14v10H1z"/><path d="M1 3l7 6 7-6" fill="none" stroke="#f7f7f7" stroke-width="1.4"/></svg>office@der-brandl.at</li>
    <li><svg viewBox="0 0 16 16"><circle cx="8" cy="8" r="7"/><path d="M1 8h14M8 1c-3 4-3 10 0 14M8 1c3 4 3 10 0 14" fill="none" stroke="#f7f7f7" stroke-width="1.2"/></svg>www.der-brandl.at</li>
    <li><svg viewBox="0 0 16 16"><path d="M8 0a5.5 5.5 0 0 1 5.5 5.5C13.5 10 8 16 8 16S2.5 10 2.5 5.5A5.5 5.5 0 0 1 8 0z"/><circle cx="8" cy="5.5" r="2" fill="#f7f7f7"/></svg><span>Leopold Hainz Gasse 14<br>2183 Melkstetten</span></li>
  </ul>

  <div class="seal" role="img" aria-label="Partnersiegel"></div>
</section>

<section class="card card-back">
  <div class="brand">
    <div class="brand-dot"></div>
    <div class="brand-text">
      <div class="brand-name">Nordwald Vermögensberatung GmbH</div>
      <div class="brand-tagline">Finanzieren, Versichern, Vorsorgen</div>
    </div>
  </div>
  <p class="register">GISA Nr. 48270315 u. 51736048</p>
</section>

</body>
</html>
```